Postcard Design

We have a chiropractic office.

We'd need our logo, main message / title being about our new hours, a call to action with a coupon or two, a doctor picture, announcement that we accept all insurance (except for medicaid), our wellness lecture schedule

New Hours:
Monday 9:00 - 1:00 3:00 - 6:00
Tuesday 3:00 - 6:00
Wednesday 9:00 - 1:00 3:00 - 6:00
Thursday 3:00 - 6:00
Friday 9:00 - 1:00 3:00 - 6:00

or could say:
Monday, Wednesday, Friday 9:00 - 1:00 3:00 - 6:00
and Tuesday / Thursday 3:00 - 6:00

Trigger Point Workshop!
Tuesday, October 21, 6:30 p.m.
Learn how to find and release those sore spots in your muscles. Dr. Halvorsen will educate you on how to find trigger points and how to help them heal. Great for people with headaches, neck and shoulder pain, lower back and hip pain. Bring a guest/partner and RSVP at (555) 417-3086.

Coupon:
Refer a friend: Free Pain Consultation and Assessment.

Coupon:
$20 off a 30 minute massage and Chiropractic Adjustment combo. Must have coupon present. Call clinic to schedule your "combo".

Website: brightpathcx.com

Pain Relief and Wellness Start Here

Target Market(s)

our current patient base

Industry/Entity Type

Insurance

Font styles to use
Other font styles liked:
• clean and modern and bold, not "script" or "decorative"

Colors
cadf82
85cae6
fdce3e

Requirements
Must have
• Ability to be mailed with a place for return address, address label and area for postage meter stamp

Return address:
4173 W Marlowe St, Broken Arrow, OK 74012

clean look, eye catching title, easy to read

ability to make old patients want to call us

Color scheme below are only suggestions but feel free to make it however you want. Perhaps a white background keeps it cleaner.

```html
<!DOCTYPE html>
<html lang="en">
<head>
<meta charset="utf-8">
<title>Brightpath Chiropractic Postcard</title>
<link rel="stylesheet" href="https://fonts.googleapis.com/css2?family=Varela+Round&family=PT+Sans+Narrow:wght@400;700&family=Archivo+Black&family=Arimo:ital,wght@0,400;0,700;1,700&display=swap">
<style>
  :root {
    --teal: #85cae6;
    --orange: #fbb45a;
    --ink: #222;
    --label: #444;
    --rule: #999;
    --paper: #fff;
  }
  * { margin: 0; padding: 0; box-sizing: border-box; }
  html, body { width: 1200px; height: 1173px; overflow: hidden; background: var(--paper); }
  .canvas { position: relative; width: 1200px; height: 1173px; font-family: "Varela Round", sans-serif; }
  .abs { position: absolute; }
  .side-label { font-family: "Varela Round", sans-serif; font-size: 24px; color: var(--label); left: 241px; }
  .card { position: absolute; left: 232px; width: 738px; border: 1px solid #555; background: var(--paper); overflow: hidden; }
  .card--front { top: 55px; height: 532px; }
  .card--back { top: 631px; height: 535px; }

  .brand { color: var(--teal); font-family: "Varela Round", sans-serif; line-height: 1; }
  .brand__name { display: block; }
  .brand__sub { display: block; text-align: right; }

  .hours-headline { color: var(--orange); font-family: "Archivo Black", sans-serif; font-size: 20px; line-height: 22px; letter-spacing: 1px; text-align: center; }
  .hours { background: var(--teal); color: #fff; font-family: "PT Sans Narrow", sans-serif; font-weight: 700; text-align: center; border-radius: 9px; }
  .hours p { line-height: 1.25; }

  .phone { color: var(--teal); font-family: "Varela Round", sans-serif; font-size: 27px; letter-spacing: 1px; }

  .doctor { background: var(--orange); }
  .doctor__photo { position: absolute; left: 10px; top: 7px; width: 130px; height: 146px; background: linear-gradient(180deg, #c9b99a 0%, #6e5a48 55%, #23262b 100%); }
  .doctor__name { position: absolute; left: 0; right: 0; bottom: 3px; text-align: center; color: #fff; font-family: "PT Sans Narrow", sans-serif; font-weight: 700; font-size: 14px; }

  .insurance { text-align: center; width: 280px; }
  .insurance__title { color: var(--teal); font-size: 17px; line-height: 18px; font-weight: 700; }
  .insurance__note { color: var(--teal); font-size: 12px; line-height: 14px; }
  .insurance__body { color: var(--orange); font-size: 13px; line-height: 16px; font-weight: 700; }

  .url-band { left: 0; top: 292px; width: 738px; height: 40px; background: var(--orange); color: #fff; font-family: "Archivo Black", sans-serif; font-size: 39px; line-height: 40px; text-align: center; letter-spacing: 8px; }
  .hero-photo { left: 0; top: 332px; width: 738px; height: 200px; background: radial-gradient(ellipse at 55% 80%, #f2b277 0%, #e79a5e 40%, #c98656 70%, #e8d9c6 100%); }

  .coupon-tab { color: #fff; font-family: "Arimo", sans-serif; font-weight: 700; font-size: 19px; text-align: center; border-radius: 5px 5px 0 0; line-height: 22px; }
  .coupon-box { border: 2px dashed; border-radius: 10px; text-align: center; font-family: "Arimo", sans-serif; font-weight: 700; }
  .coupon-box--teal { border-color: var(--teal); }
  .coupon-box--orange { border-color: var(--orange); }
  .c-orange { color: var(--orange); }
  .c-teal { color: var(--teal); }
  .fine { font-family: "Arimo", sans-serif; font-style: italic; font-weight: 700; font-size: 11px; }

  .workshop { left: 368px; top: 92px; width: 232px; font-family: "Arimo", sans-serif; }
  .workshop__title { color: var(--orange); font-weight: 700; font-size: 16px; line-height: 19px; }
  .workshop__date { color: var(--teal); font-weight: 700; font-size: 13px; line-height: 17px; margin-top: 2px; }
  .workshop__body { color: var(--ink); font-size: 11px; line-height: 14px; margin-top: 5px; }

  .vertical-url { left: 568px; top: 898px; transform: translate(-50%, -50%) rotate(-90deg); white-space: nowrap; color: var(--teal); font-family: "Arimo", sans-serif; font-weight: 700; font-size: 38px; letter-spacing: 3px; }
  .divider { left: 364px; top: 84px; width: 2px; height: 420px; background: var(--rule); }
  .return-address { left: 368px; top: 25px; font-family: "Arimo", sans-serif; font-weight: 700; font-size: 12px; line-height: 15px; color: var(--ink); }
  .return-address em { font-style: italic; }
  .stamp { left: 618px; top: 25px; width: 93px; height: 99px; border: 1px solid #aaa; }
  .address-line { left: 399px; width: 280px; height: 2px; background: var(--rule); }
</style>
</head>
<body>
<div class="canvas">
  <div class="abs side-label" style="top:24px;">front</div>

  <section class="card card--front">
    <div class="abs brand" style="left:26px; top:62px;">
      <span class="brand__name" style="font-size:76px;">brightpath</span>
      <span class="brand__sub" style="font-size:21px; margin-top:2px;">chiropractic</span>
    </div>

    <div class="abs hours-headline" style="left:26px; top:172px; width:363px;">NEW OFFICE HOURS!</div>

    <div class="abs hours" style="left:26px; top:197px; width:363px; height:44px; font-size:16px; padding-top:3px;">
      <p>Monday, Wednesday, Friday 9:00 - 1:00 3:00 - 6:00</p>
      <p>Tuesday / Thursday 3:00 - 6:00</p>
    </div>

    <div class="abs phone" style="left:68px; top:253px;">tel. (555) 417-3086</div>

    <div class="abs doctor" style="left:501px; top:0; width:152px; height:173px;">
      <div class="doctor__photo" role="img" aria-label="Portrait photo of Dr. Marcus Halvorsen"></div>
      <div class="doctor__name">Dr. Marcus Halvorsen</div>
    </div>

    <div class="abs insurance" style="left:436px; top:177px;">
      <p class="insurance__title">WE ACCEPT<br>ALL INSURANCE!</p>
      <p class="insurance__note">(except Medicaid)</p>
      <p class="insurance__body">Whether you're searching<br>for effective pain relief or<br>a way to boost whole body wellness<br>Brightpath Chiropractic can help.</p>
    </div>

    <div class="abs url-band">www.brightpathcx.com</div>
    <div class="abs hero-photo" role="img" aria-label="Photo of a therapist's hands massaging a patient's upper back"></div>
  </section>

  <div class="abs side-label" style="top:601px;">back</div>

  <section class="card card--back">
    <div class="abs brand" style="left:31px; top:55px;">
      <span class="brand__name" style="font-size:50px;">brightpath</span>
      <span class="brand__sub" style="font-size:12px; margin-top:3px;">chiropractic</span>
    </div>

    <div class="abs hours" style="left:31px; top:132px; width:232px; height:29px; font-size:10px; padding-top:2px; border-radius:6px;">
      <p>Monday, Wednesday, Friday 9:00 - 1:00 3:00 - 6:00</p>
      <p>Tuesday / Thursday 3:00 - 6:00</p>
    </div>

    <div class="abs coupon-tab" style="left:177px; top:178px; width:112px; height:23px; background:var(--teal);">coupon</div>
    <div class="abs coupon-box coupon-box--teal" style="left:31px; top:196px; width:247px; height:112px; padding-top:8px;">
      <p class="c-orange" style="font-size:23px; line-height:24px;">REFER A FRIEND</p>
      <p class="c-teal" style="font-size:20px; line-height:23px;">Free Pain<br>Consultation<br>and Assessment*</p>
    </div>
    <div class="abs fine c-teal" style="left:36px; top:309px;">* Must have coupon present</div>

    <div class="abs coupon-tab" style="left:177px; top:351px; width:112px; height:23px; background:var(--orange);">coupon</div>
    <div class="abs coupon-box coupon-box--orange" style="left:31px; top:369px; width:247px; height:112px; padding-top:6px;">
      <p class="c-teal" style="font-family:'Archivo Black',sans-serif; font-size:31px; line-height:34px; letter-spacing:1px;">$20 OFF</p>
      <p class="c-orange" style="font-size:15px; line-height:16px;">a 30 Minute massage and<br>Chiropractic<br>Adjustment Combo</p>
      <p class="fine c-teal" style="margin-top:3px;">Call clinic to schedule your "combo"*</p>
    </div>
    <div class="abs fine c-orange" style="left:29px; top:484px;">* Must have coupon present</div>

    <div class="abs divider"></div>
    <div class="abs return-address">
      BRIGHTPATH CHIROPRACTIC<br>
      <em>4173 W Marlowe St</em><br>
      <em>Broken Arrow, OK 74012</em>
    </div>
    <div class="abs workshop">
      <p class="workshop__title">Trigger Point Workshop!</p>
      <p class="workshop__date">Tuesday, October 21, 6:30 p.m.</p>
      <p class="workshop__body">Learn how to find and release those sore spots in your muscles. Dr. Halvorsen will educate you on how to find trigger points and how to help them heal. Great for people with headaches, neck and shoulder pain, lower back and hip pain. Bring a guest/partner and RSVP at (555) 417-3086.</p>
    </div>
    <div class="abs stamp"></div>
    <div class="abs address-line" style="top:326px;"></div>
    <div class="abs address-line" style="top:379px;"></div>
    <div class="abs address-line" style="top:434px;"></div>
  </section>

  <div class="abs vertical-url">www.brightpathcx.com</div>
</div>
</body>
</html>
```